Founder / concept developer needs business card // Consultant needs VCARD

I need a business card for me as a founding consultant in Berlin. I advise entrepreneurs, especially in the design of business ideas, business plans or financing applications. More information about this in the annexes. My USP: I design / structure complex ideas and projects convincingly so that my client is successful. I want to communicate professionalism, effectiveness and clarity. Colors like from the range BLACK-GRAY-GREEN. I am 27 years old, I have studied business for 7 years. Attachments: - Business card design (only idea, do not focus on it) - Website screenshot (only idea, do not focus on it)

Target Market(s)

Target group: Founder (20-50 yrs, m / w, needy, in "break-up phase") and CONTRACTOR / "financier" (30-55 yrs, m / w, often public service "routine-oriented"). The foundations are in quite different industries: digital, craft, tourism, retail, services, etc. Almost all German.

Industry/Entity Type

Consultant

Contact Information for Business Card

Lukas Brenner
M. Sc., International Business Administration
Gründungsberater, Konzeptentwickler
www.falkor-plan.de
kontakt@falkor-plan.de
Tel. 0157 284 3361

Colors

Designer to choose colors to be used in the design.

Requirements
Must have
• Professionalism, persuasiveness, clarity
Nice to have
• memorability
Should not have
• Schnörkelei

```html
<!DOCTYPE html>
<html lang="de">
<head>
<meta charset="utf-8">
<title>Lukas Brenner – Visitenkarte</title>
<link href="https://fonts.googleapis.com/css2?family=Work+Sans:wght@400;500&display=swap" rel="stylesheet">
<style>
  :root {
    --bg: #2b2b2b;
    --green: #3ea84a;
    --green-dark: #2f8f3b;
    --paper: #ffffff;
    --ink: #7a7a7a;
    --on-green: #e9f6ea;
  }
  * { margin: 0; padding: 0; box-sizing: border-box; }
  html, body { width: 1200px; height: 930px; overflow: hidden; }
  body {
    background: var(--bg);
    font-family: "Work Sans", Arial, sans-serif;
    position: relative;
  }
  .card {
    position: absolute;
    width: 600px;
    height: 345px;
    box-shadow: 0 10px 30px rgba(0,0,0,.45);
  }
  .card-back {
    left: 90px; top: 90px;
    background: var(--green);
  }
  .card-front {
    left: 510px; top: 485px;
    background: var(--paper);
  }
  .brand {
    position: absolute;
    display: flex;
    align-items: center;
    gap: 10px;
    font-weight: 500;
    font-size: 24px;
    letter-spacing: .02em;
  }
  .brand-square {
    width: 18px; height: 18px;
  }
  .card-back .brand {
    left: 50%; top: 132px;
    transform: translateX(-50%);
    color: var(--paper);
  }
  .card-back .brand-square { background: var(--paper); }
  .card-back .website {
    position: absolute;
    left: 0; right: 0; bottom: 36px;
    text-align: center;
    padding-left: 120px;
    color: var(--on-green);
    font-size: 14px;
    letter-spacing: .04em;
  }
  .card-front .brand {
    left: 60px; top: 150px;
    color: var(--green);
  }
  .card-front .brand-square { background: var(--green); }
  .contact {
    position: absolute;
    left: 310px; top: 92px;
    color: var(--ink);
    font-size: 13px;
    line-height: 1.35;
  }
  .contact .name {
    color: var(--green);
    font-size: 25px;
    font-weight: 500;
    margin-bottom: 8px;
    letter-spacing: .01em;
  }
  .contact .degree { margin-bottom: 8px; }
  .contact .roles { margin-bottom: 10px; font-size: 14px; }
  .contact ul { list-style: none; }
  .contact li {
    display: flex; align-items: center; gap: 10px;
    font-size: 14px; line-height: 1.45;
  }
  .contact li svg { width: 11px; height: 11px; flex: none; }
  .contact .accent { color: var(--green); }
</style>
</head>
<body>

  <section class="card card-back">
    <div class="brand"><span class="brand-square"></span>Falkor Plan</div>
    <p class="website">www.falkor-plan.de</p>
  </section>

  <section class="card card-front">
    <div class="brand"><span class="brand-square"></span>Falkor Plan</div>
    <div class="contact">
      <h1 class="name">Lukas Brenner</h1>
      <p class="degree">M. Sc.,<br>International Business Administration</p>
      <p class="roles">Gründungsberater,<br>Konzeptentwickler</p>
      <ul>
        <li>
          <svg viewBox="0 0 12 12" aria-hidden="true"><path d="M2.5 1 L4.5 1 L5 3.5 L3.8 4.5 Q5 7 7.5 8.2 L8.5 7 L11 7.5 L11 9.5 Q10.5 11 9 11 Q1 10 1 3 Q1 1.5 2.5 1Z" fill="var(--green)"/></svg>
          0157 284 3361
        </li>
        <li>
          <svg viewBox="0 0 12 12" aria-hidden="true"><rect x="1" y="2.5" width="10" height="7" fill="none" stroke="var(--green)" stroke-width="1.3"/><path d="M1 2.5 L6 6.5 L11 2.5" fill="none" stroke="var(--green)" stroke-width="1.3"/></svg>
          kontakt@falkor-plan.de
        </li>
        <li>
          <svg viewBox="0 0 12 12" aria-hidden="true"><circle cx="6" cy="6" r="5" fill="none" stroke="var(--green)" stroke-width="1.2"/><ellipse cx="6" cy="6" rx="2.2" ry="5" fill="none" stroke="var(--green)" stroke-width="1"/><path d="M1 6 H11" stroke="var(--green)" stroke-width="1"/></svg>
          <span>www.<span class="accent">falkor-plan</span>.de</span>
        </li>
      </ul>
    </div>
  </section>

</body>
</html>
```